Silver Fern Counseling business cards

Dana Korvath, LCPC, NCC
(410)555-0187
www.silverferncounseling.example
dana@silverferncounseling.example

Business cards. I would like it on the same background as pictured. Not on a white business card. I have attached the logo that was done by another designer with artflockly. I am open to looking at single-sided and double-sided designs.

Target Market(s)

teenagers and adults

Industry/Entity Type

mental health

Contact Information for Business Card

Dana Korvath, LCPC, NCC (410)555-0187 dana@silverferncounseling.example

Font styles to use
Other font styles liked:
• Cinzel

Colors

Designer to choose colors to be used in the design.

Requirements
Must have
• logo that is attached

```html
<!DOCTYPE html>
<html lang="en">
<head>
<meta charset="utf-8">
<title>Silver Fern Counseling — Business Cards</title>
<link href="https://fonts.googleapis.com/css2?family=Cinzel:wght@400;600&family=Cormorant+SC:wght@400;500&display=swap" rel="stylesheet">
<style>
  :root {
    --page: #f6f6f6;
    --card: #1f2a33;
    --silver: #c8c9cb;
    --rule: #9ea3a7;
    --coral: #e0745a;
    --teal: #3f9a94;
    --blue: #3a6e86;
    --green: #557a3c;
    --icon-grey: #a9adb0;
  }
  * { margin: 0; padding: 0; box-sizing: border-box; }
  html, body { width: 1200px; height: 371px; overflow: hidden; background: var(--page); }
  .sheet { position: relative; width: 1200px; height: 371px; }

  .card {
    position: absolute; top: 20px; height: 331px;
    background: var(--card); overflow: hidden;
    box-shadow: 0 1px 3px rgba(0,0,0,.15);
  }
  .card--front { left: 28px; width: 553px; }
  .card--back { left: 621px; width: 555px; }

  .leaf-cluster {
    position: absolute; left: 0; top: 100px; width: 190px; height: 231px;
    border-radius: 55% 60% 0 0 / 45% 50% 0 0;
    background:
      radial-gradient(circle at 40% 82%, var(--coral) 0 30%, transparent 31%),
      radial-gradient(circle at 72% 42%, var(--green) 0 20%, transparent 21%),
      radial-gradient(circle at 28% 38%, var(--blue) 0 28%, transparent 29%),
      linear-gradient(160deg, var(--teal), var(--blue));
    opacity: .95;
  }

  .wordmark {
    position: absolute; display: flex; flex-direction: column; align-items: center;
    font-family: "Cinzel", serif; font-weight: 600; color: var(--silver);
    white-space: nowrap; text-align: center; line-height: 1.15;
    transform: translateX(-50%);
  }
  .wordmark__dot { border-radius: 50%; background: var(--silver); }
  .card--front .wordmark { left: 356px; top: 100px; font-size: 24px; letter-spacing: 1.5px; }
  .card--front .wordmark__dot { width: 72px; height: 72px; margin-bottom: 22px; }
  .card--back .wordmark { left: 131px; top: 48px; font-size: 16px; letter-spacing: 1px; }
  .card--back .wordmark__dot { width: 50px; height: 50px; margin-bottom: 14px; }

  .holder-name {
    position: absolute; right: 55px; top: 160px;
    font-family: "Cinzel", serif; font-weight: 400; font-size: 26px; letter-spacing: 1px; color: var(--silver);
  }
  .credentials {
    position: absolute; right: 55px; top: 201px;
    font-family: "Cormorant SC", serif; font-size: 19px; letter-spacing: 1px; color: var(--silver);
  }
  .frame-rule-h { position: absolute; left: 68px; top: 195px; width: 440px; height: 1.5px; background: var(--rule); }
  .frame-rule-v { position: absolute; left: 68px; top: 195px; width: 1.5px; height: 140px; background: var(--rule); }

  .contact {
    position: absolute; left: 58px; display: flex; align-items: center; gap: 8px;
    font-family: "Cormorant SC", serif; color: var(--silver); font-size: 18px; letter-spacing: 1.2px;
  }
  .contact--phone { top: 232px; }
  .contact--email { top: 263px; font-size: 15px; letter-spacing: 1.4px; }
  .contact__icon { width: 22px; height: 22px; display: flex; align-items: center; justify-content: center; flex: none; }
  .contact__icon--phone { background: var(--coral); }
  .contact__icon--email { background: var(--icon-grey); }
</style>
</head>
<body>
<div class="sheet">
  <section class="card card--front">
    <div class="leaf-cluster" role="img" aria-label="Cluster of coral, teal, blue and green leaves"></div>
    <div class="wordmark"><span class="wordmark__dot"></span><span>Silver Fern</span><span>Counseling</span></div>
  </section>

  <section class="card card--back">
    <div class="wordmark"><span class="wordmark__dot"></span><span>Silver Fern</span><span>Counseling</span></div>
    <h1 class="holder-name">Dana Korvath</h1>
    <div class="frame-rule-h"></div>
    <div class="frame-rule-v"></div>
    <p class="credentials">LCPC, NCC</p>
    <div class="contact contact--phone">
      <span class="contact__icon contact__icon--phone">
        <svg width="13" height="13" viewBox="0 0 24 24"><path fill="#1f2a33" d="M6.6 10.8a15 15 0 0 0 6.6 6.6l2.2-2.2a1 1 0 0 1 1-.25 11.4 11.4 0 0 0 3.6.57 1 1 0 0 1 1 1V20a1 1 0 0 1-1 1A17 17 0 0 1 3 4a1 1 0 0 1 1-1h3.5a1 1 0 0 1 1 1c0 1.250.2 2.450.57 3.57a1 1 0 0 1-.25 1z"/></svg>
      </span>
      <span>(410)555-0187</span>
    </div>
    <div class="contact contact--email">
      <span class="contact__icon contact__icon--email">
        <svg width="14" height="10" viewBox="0 0 14 10"><rect x=".75" y=".75" width="12.5" height="8.5" fill="none" stroke="#1f2a33" stroke-width="1.3"/><path d="M.75.75 7 5.5 13.25.75M.75 9.25 5.3 4.4M13.25 9.25 8.7 4.4" fill="none" stroke="#1f2a33" stroke-width="1.1"/></svg>
      </span>
      <span>dana@silverferncounseling.example</span>
    </div>
  </section>
</div>
</body>
</html>
```